A4 6 page tri-fold brochure for security screen company

Brochure design and layout for a new company based in the UAE called Harborline Panels. We make clear mesh security screen doors and windows that aesthetically blend with the house, like a fly screen, rather than a traditional heavy looking security screen. We want to project an image of safety and security but with warmth and humanity to it, not just something clinical. Copy hasn't been written yet so use dummy text or pull and adjust copy form our website www.harborlinepanels.example.
Target market: home owners, financially comfortable, possibly with young children or pets.
Purpose of brochure: to have potential clients contact us (via phone, whatsapp, email or through our website) to arrange a free measure and quote.
More details provided in attached word doc brief and product images, logos etc, attached also.
Please see attached brief.

Target Market(s)

Home owners, financially comfortable, possibly with young children or pets.

Industry/Entity Type

Home Improvement

Font styles to use
Serif
Sans Serif

Colors
0255a3
3176b5
85acd3
cfdfed
eaf1f7

Requirements
Must have
• Good clear images with detailed close ups (or call outs) of specific details such as the mesh and locks.
• Contact details to include website www.harborlinepanels.example, phone number: +971 50 318 2609, email address: oliver@harborlinepanels.example
Nice to have
• If your are comfortable using and adjusting the appropriate copy from our website please do so.
• Images - I've included a lot of images so please choose the most appropriate to help sell the product. Some of the better images I like are: _DSC2929, French_Windows, HARBORLINE_PANELS-3204, HARBORLINE_PANELS-3231, HARBORLINE_PANELS-3345, HARBORLINE_PANELS-3354, HARBORLINE_PANELS-3401, Girls room windows1, Girls room windows2, IMG_2968. Please don't limit yourself to these images and use the ones you feel best fit.
Should not have
• Please see attached brief.

```html
<!DOCTYPE html>
<html lang="en">
<head>
<meta charset="utf-8">
<title>Harborline Panels – Tri-fold Brochure</title>
<link href="https://fonts.googleapis.com/css2?family=Michroma&family=Montserrat:wght@400;600;700&display=swap" rel="stylesheet">
<style>
:root{
  --blue-deep:#0255a3;
  --blue:#3176b5;
  --blue-mid:#85acd3;
  --blue-pale:#cfdfed;
  --blue-mist:#eaf1f7;
  --navy:#1d3557;
  --grey:#a9aaad;
  --grey-light:#c9cacc;
  --ink:#3c3c3c;
  --paper:#ffffff;
  --backdrop:#e4e4e4;
  --gold:#c99a2e;
}
*{box-sizing:border-box;margin:0;padding:0}
html,body{width:1200px;height:1200px;overflow:hidden;background:var(--backdrop)}
body{font-family:"Montserrat",sans-serif;color:var(--ink);position:relative}
.spread{position:absolute;left:40px;width:1120px;height:396px;display:grid;grid-template-columns:repeat(3,1fr);background:var(--paper);box-shadow:0 6px 18px rgba(0,0,0,.18)}
.spread--outside{top:170px}
.spread--inside{top:630px}
.panel{position:relative;overflow:hidden;border-right:1px solid #ececec}
.panel:last-child{border-right:none}
.heading{font-family:"Michroma",sans-serif;color:var(--blue-deep);font-size:10px;letter-spacing:.5px;text-transform:uppercase}
.heading--rule{border-bottom:1.5px solid var(--blue);padding-bottom:3px;display:inline-block}
.body-text{font-size:5.6px;line-height:1.45;color:#555}
.photo{position:absolute;clip-path:polygon(25% 0,75% 0,100% 50%,75% 100%,25% 100%,0 50%)}
.photo--room{background:linear-gradient(135deg,#e9dfcf,#b7a58a 55%,#6e7a80)}
.photo--door{background:linear-gradient(135deg,#cbb79a,#6d4a33 60%,#3b2a20)}
.photo--window{background:linear-gradient(135deg,#d9e6ef,#8fb0c4 50%,#e8e2d6)}
.photo--mesh{background:linear-gradient(135deg,#6b7380,#3a404a 60%,#7b838f)}
.hex-line{position:absolute;fill:none;stroke:var(--blue);stroke-width:2}
/* product details flap */
.details-band{position:absolute;left:0;top:20px;width:100%;height:60px;background:var(--blue);clip-path:polygon(0 0,100% 0,100% 55%,40% 100%,0 80%)}
.details-title{position:absolute;left:28px;top:30px;font-family:"Michroma",sans-serif;color:#fff;font-size:18px;line-height:1}
.details-title small{display:block;font-size:11px;margin-top:4px}
.detail-item{position:absolute;width:175px}
/* back panel */
.warranty-text{position:absolute;left:22px;top:22px;width:300px;font-size:7.5px;line-height:1.5;color:#333}
.warranty-text b{font-weight:700}
.warranty-badge{position:absolute;left:40px;top:80px;width:68px;height:68px;border-radius:50%;background:radial-gradient(circle,#e7c05a,var(--gold) 65%,#8a6516)}
.brand-band{position:absolute;left:0;top:170px;width:100%;height:70px;background:var(--blue);clip-path:polygon(0 0,62% 0,72% 50%,62% 100%,0 100%)}
.brand-name{position:absolute;left:26px;top:194px;font-family:"Montserrat",sans-serif;font-weight:700;color:#fff;font-size:15px;letter-spacing:2px}
.contact-block{position:absolute;left:0;bottom:0;width:100%;height:140px;background:linear-gradient(160deg,var(--grey-light),var(--grey));padding:20px 22px;color:#fff}
.contact-lead{font-family:"Michroma",sans-serif;font-size:10px}
.contact-lead span{color:var(--blue-deep)}
.contact-phone{font-family:"Michroma",sans-serif;font-size:20px;margin:10px 0 8px}
.contact-line{font-size:9px;font-weight:600;margin-top:3px}
/* cover */
.cover-photo{position:absolute;left:0;top:0;width:100%;height:215px;background:linear-gradient(180deg,#a9cbe6 0%,#dfe9f1 35%,#efe4cf 60%,#c9b89a 100%);clip-path:polygon(14% 0,100% 0,100% 100%,0 100%,0 20%)}
.cover-accent{position:absolute;left:0;top:40px;width:26px;height:180px;background:var(--blue-deep);clip-path:polygon(100% 0,100% 100%,0 85%,0 15%)}
.cover-mesh{left:22px;top:130px;width:140px;height:118px}
.cover-grey{position:absolute;right:0;top:150px;width:90px;height:90px;background:#8e8f92;clip-path:polygon(50% 0,100% 0,100% 100%,0 100%)}
.cover-brand{position:absolute;left:175px;top:262px;font-family:"Montserrat",sans-serif;font-weight:700;font-size:17px;color:var(--blue-deep);letter-spacing:2px;line-height:1.05}
.cover-brand::before{content:"";display:inline-block;width:12px;height:12px;background:var(--blue-deep);margin-right:6px}
.cover-tag{position:absolute;left:22px;top:305px;font-family:"Michroma",sans-serif;font-size:9px;color:var(--navy)}
.cover-tag-band{position:absolute;left:22px;top:322px;background:var(--blue);color:#fff;font-family:"Montserrat",sans-serif;font-style:italic;font-weight:700;font-size:14px;padding:3px 10px}
.cover-tag-foot{position:absolute;left:22px;top:350px;font-family:"Michroma",sans-serif;font-size:9px;color:var(--navy)}
.cover-web{position:absolute;left:22px;top:368px;font-size:8px;font-weight:700;color:var(--blue-deep);letter-spacing:2px}
/* inside */
.info-block{position:absolute;left:22px;width:325px}
.hero-photo{position:absolute;left:0;bottom:0;width:150%;height:175px;background:linear-gradient(180deg,#ece4d2 0%,#d9cdb4 45%,#7d8d96 70%,#4a4f52 100%);clip-path:polygon(0 45%,48% 0,100% 20%,100% 100%,0 100%);z-index:1}
.hero-mesh{left:40px;top:198px;width:130px;height:110px;z-index:2}
.hero-blue{position:absolute;right:0;bottom:0;width:115px;height:100px;background:var(--blue-deep);clip-path:polygon(0 0,100% 60%,100% 100%,20% 100%);z-index:2}
.product-row{position:absolute}
</style>
</head>
<body>

<!-- OUTSIDE SPREAD -->
<section class="spread spread--outside" aria-label="Brochure outside">
  <!-- Product details flap -->
  <div class="panel panel--details">
    <div class="details-band"></div>
    <h2 class="details-title">PRODUCT<small>DETAILS</small></h2>
    <svg class="hex-line" style="left:250px;top:40px;stroke:var(--navy)" width="80" height="70" viewBox="0 0 80 70"><polygon points="20,2 60,2 78,35 60,68 20,68 2,35"/></svg>

    <div class="photo photo--window" style="left:20px;top:105px;width:110px;height:92px" role="img" aria-label="Photo of a window fitted with a mesh screen"></div>
    <svg class="hex-line" style="left:18px;top:170px" width="50" height="42" viewBox="0 0 50 42"><polygon points="13,2 37,2 48,21 37,40 13,40 2,21"/></svg>
    <div class="detail-item" style="left:160px;top:118px"><h3 class="heading">Lorem Ipsum</h3><p class="body-text">Lorem ipsum is simply dummy text of the printing and typesetting industry. Lorem ipsum has been the industry's standard dummy text ever since the 1500s.</p></div>

    <div class="photo photo--room" style="left:90px;top:195px;width:110px;height:92px" role="img" aria-label="Photo of a sliding screen door opening onto a garden"></div>
    <svg class="hex-line" style="left:160px;top:262px" width="50" height="42" viewBox="0 0 50 42"><polygon points="13,2 37,2 48,21 37,40 13,40 2,21"/></svg>
    <div class="detail-item" style="left:210px;top:210px;width:150px"><h3 class="heading">Lorem Ipsum</h3><p class="body-text">Lorem ipsum is simply dummy text of the printing and typesetting industry. Lorem ipsum has been the industry's standard dummy text ever since the 1500s.</p></div>

    <div class="photo photo--window" style="left:20px;top:290px;width:110px;height:92px" role="img" aria-label="Photo of French windows with screens"></div>
    <div class="detail-item" style="left:160px;top:305px"><h3 class="heading">Lorem Ipsum</h3><p class="body-text">Lorem ipsum is simply dummy text of the printing and typesetting industry. Lorem ipsum has been the industry's standard dummy text ever since the 1500s.</p></div>
  </div>

  <!-- Back panel -->
  <div class="panel panel--back">
    <p class="warranty-text">Should you have any problems with your Harborline Panels, we offer a <b>10 year warranty</b> on all stainless steel mesh and aluminium products and <b>1 year</b> on component parts.</p>
    <div class="warranty-badge" aria-hidden="true"></div>
    <div class="brand-band"></div>
    <p class="brand-name">HARBORLINE PANELS</p>
    <svg class="hex-line" style="left:250px;top:200px;stroke:#fff" width="56" height="48" viewBox="0 0 56 48"><polygon points="14,2 42,2 54,24 42,46 14,46 2,24"/></svg>
    <div class="contact-block">
      <p class="contact-lead">CONTACT US FOR A <span>FREE QUOTE:</span></p>
      <p class="contact-phone">+971 50 318 2609</p>
      <p class="contact-line">www.harborlinepanels.example</p>
      <p class="contact-line">oliver@harborlinepanels.example</p>
    </div>
  </div>

  <!-- Front cover -->
  <div class="panel panel--cover">
    <div class="cover-photo" role="img" aria-label="Photo of a two-storey cream villa with balconies under a blue sky"></div>
    <div class="cover-accent"></div>
    <div class="cover-grey"></div>
    <div class="photo photo--mesh cover-mesh" role="img" aria-label="Close-up of stainless steel security mesh"></div>
    <svg class="hex-line" style="left:18px;top:126px;stroke:var(--blue-deep);stroke-width:3" width="148" height="126" viewBox="0 0 148 126"><polygon points="37,2 111,2 146,63 111,124 37,124 2,63"/></svg>
    <p class="cover-brand">HARBORLINE<br>PANELS</p>
    <p class="cover-tag">SERIOUSLY STRONG SCREENS</p>
    <p class="cover-tag-band">that let the breeze in and</p>
    <p class="cover-tag-foot">KEEP INTRUDERS (AND BUGS) OUT!</p>
    <p class="cover-web">www.harborlinepanels.example</p>
  </div>
</section>

<!-- INSIDE SPREAD -->
<section class="spread spread--inside" aria-label="Brochure inside">
  <div class="panel panel--info">
    <div class="info-block" style="top:18px">
      <h2 class="heading heading--rule">General Info</h2>
      <p class="body-text" style="margin-top:4px">Lorem ipsum is simply dummy text of the printing and typesetting industry. Lorem ipsum has been the industry's standard dummy text ever since the 1500s. It has survived not only five centuries, but also the leap into electronic typesetting.</p>
    </div>
    <div class="info-block" style="top:78px">
      <h2 class="heading heading--rule">Primary Benefits</h2>
      <p class="body-text" style="margin-top:4px">Lorem ipsum is simply dummy text of the printing and typesetting industry. Lorem ipsum has been the industry's standard dummy text ever since the 1500s. It has survived not only five centuries, but also the leap into electronic typesetting.</p>
      <p class="body-text" style="margin-top:4px">Lorem ipsum is simply dummy text of the printing and typesetting industry. Lorem ipsum has been the industry's standard dummy text ever since the 1500s.</p>
    </div>
    <div class="hero-photo" role="img" aria-label="Photo of a villa terrace with screened sliding doors and outdoor furniture"></div>
    <div class="photo photo--mesh hero-mesh" role="img" aria-label="Close-up of woven security mesh"></div>
    <svg class="hex-line" style="left:130px;top:250px;stroke:#fff;z-index:3" width="70" height="60" viewBox="0 0 70 60"><polygon points="18,2 52,2 68,30 52,58 18,58 2,30"/></svg>
  </div>

  <div class="panel panel--sliding">
    <div style="position:absolute;left:0;bottom:0;width:100%;height:175px;background:linear-gradient(180deg,#d9cdb4,#7d8d96 50%,#4a4f52);clip-path:polygon(0 20%,40% 0,100% 75%,100% 100%,0 100%)" role="img" aria-label="Continuation of the villa terrace photo"></div>
    <div class="hero-blue"></div>
    <h2 class="heading heading--rule" style="position:absolute;left:22px;top:18px">Sliding Screen Doors</h2>
    <div class="photo photo--room" style="left:20px;top:45px;width:100px;height:84px" role="img" aria-label="Photo of a sliding screen door from inside a room"></div>
    <svg class="hex-line" style="left:18px;top:105px" width="46" height="38" viewBox="0 0 46 38"><polygon points="12,2 34,2 44,19 34,36 12,36 2,19"/></svg>
    <div class="product-row" style="left:135px;top:60px;width:215px">
      <h3 class="heading">Lorem Ipsum</h3>
      <p class="body-text">Lorem ipsum is simply dummy text of the printing and typesetting industry. Lorem ipsum has been the industry's standard dummy text ever since the 1500s. It has survived not only five centuries, but also the leap into electronic typesetting.</p>
    </div>
    <div class="product-row" style="left:20px;top:140px;width:220px;text-align:right">
      <h3 class="heading">Lorem Ipsum</h3>
      <p class="body-text">Lorem ipsum is simply dummy text of the printing and typesetting industry. Lorem ipsum has been the industry's standard dummy text ever since the 1500s. It has survived not only five centuries, but also the leap into electronic typesetting.</p>
    </div>
    <div class="photo photo--door" style="left:255px;top:128px;width:100px;height:84px" role="img" aria-label="Photo of screened sliding doors on a patio"></div>
    <svg class="hex-line" style="left:252px;top:188px" width="46" height="38" viewBox="0 0 46 38"><polygon points="12,2 34,2 44,19 34,36 12,36 2,19"/></svg>
  </div>

  <div class="panel panel--range">
    <div class="photo photo--door" style="left:20px;top:20px;width:110px;height:92px" role="img" aria-label="Photo of hinged screen doors in wood-tone frames"></div>
    <svg class="hex-line" style="left:18px;top:86px" width="50" height="42" viewBox="0 0 50 42"><polygon points="13,2 37,2 48,21 37,40 13,40 2,21"/></svg>
    <div class="product-row" style="left:150px;top:32px;width:200px">
      <h2 class="heading heading--rule">Hinged Doors</h2>
      <h3 class="heading" style="font-size:8px;margin-top:3px">Lorem Ipsum</h3>
      <p class="body-text">Lorem ipsum is simply dummy text of the printing and typesetting industry. Lorem ipsum has been the industry's standard dummy text ever since the 1500s.</p>
    </div>

    <div class="photo photo--room" style="left:70px;top:140px;width:110px;height:92px" role="img" aria-label="Photo of French doors fitted with clear mesh screens"></div>
    <svg class="hex-line" style="left:68px;top:206px" width="50" height="42" viewBox="0 0 50 42"><polygon points="13,2 37,2 48,21 37,40 13,40 2,21"/></svg>
    <div class="product-row" style="left:200px;top:150px;width:155px">
      <h2 class="heading heading--rule">French Doors</h2>
      <h3 class="heading" style="font-size:8px;margin-top:3px">Lorem Ipsum</h3>
      <p class="body-text">Lorem ipsum is simply dummy text of the printing and typesetting industry. Lorem ipsum has been the industry's standard dummy text ever since the 1500s.</p>
    </div>

    <div class="photo photo--window" style="left:20px;top:270px;width:110px;height:92px" role="img" aria-label="Photo of French windows looking out to neighbouring villas"></div>
    <svg class="hex-line" style="left:50px;top:330px" width="50" height="42" viewBox="0 0 50 42"><polygon points="13,2 37,2 48,21 37,40 13,40 2,21"/></svg>
    <div class="product-row" style="left:150px;top:282px;width:200px">
      <h2 class="heading heading--rule">French Windows</h2>
      <h3 class="heading" style="font-size:8px;margin-top:3px">Lorem Ipsum</h3>
      <p class="body-text">Lorem ipsum is simply dummy text of the printing and typesetting industry. Lorem ipsum has been the industry's standard dummy text ever since the 1500s.</p>
    </div>
  </div>
</section>

</body>
</html>
```